Ferncrest Dental, LLC business card project

Business card to be designed with current logo.
Dental office- please keep design of card that looks clean and professional.
Please include the following info:
Ferncrest Dental, LLC
Dr. Lorna Pettigrew
2871 Marlowe Street
Harrowgate, VT 05999
555-555-0193
ferncrestdental.office@examplemail.test
Hello everyone-
Reason: Just got back from overseas- will look at all designs and provide feedback. Thank you!
Reason: Polling my friends for the final selection-
thank you to all those that participated- so many talented designers!

```html
<!DOCTYPE html>
<html lang="en">
<head>
<meta charset="utf-8">
<title>Ferncrest Dental, LLC — Business Card</title>
<link rel="stylesheet" href="https://fonts.googleapis.com/css2?family=Questrial&family=Roboto+Condensed:wght@300;400&display=swap">
<style>
  :root {
    --backdrop: #e6e6e6;
    --card-white: #ffffff;
    --card-green: #b4d334;
    --brand-green: #6aa934;
    --mark-pale: #d9ea9a;
    --ink-light: #ffffff;
    --card-shadow: rgba(0, 0, 0, 0.18);
  }
  * { box-sizing: border-box; margin: 0; padding: 0; }
  html, body {
    width: 1200px;
    height: 900px;
    overflow: hidden;
    background: var(--backdrop);
  }
  .canvas {
    position: relative;
    width: 1200px;
    height: 900px;
  }
  .card {
    position: absolute;
    left: 300px;
    width: 600px;
    height: 343px;
    box-shadow: 0 4px 14px var(--card-shadow);
    overflow: hidden;
  }
  .card--front {
    top: 90px;
    background: var(--card-white);
    display: flex;
    align-items: center;
    justify-content: center;
  }
  .card--back {
    top: 467px;
    background: var(--card-green);
  }
  .brand {
    display: flex;
    align-items: center;
    gap: 16px;
    margin-top: -20px;
  }
  .brand__dot {
    width: 22px;
    height: 22px;
    border-radius: 50%;
    background: var(--brand-green);
  }
  .brand__name {
    font-family: "Questrial", sans-serif;
    font-weight: 400;
    font-size: 40px;
    color: var(--brand-green);
    letter-spacing: -0.5px;
  }
  .back-emblem {
    position: absolute;
    left: 48px;
    top: 40px;
    width: 150px;
    height: 150px;
    border-radius: 50%;
    background: var(--mark-pale);
    opacity: 0.75;
  }
  .holder {
    position: absolute;
    left: 300px;
    top: 112px;
    font-family: "Questrial", sans-serif;
    font-weight: 400;
    font-size: 25px;
    color: var(--ink-light);
    white-space: nowrap;
  }
  .contact {
    position: absolute;
    left: 292px;
    top: 186px;
    list-style: none;
    font-family: "Roboto Condensed", sans-serif;
    font-weight: 300;
    font-size: 17px;
    line-height: 25px;
    color: var(--ink-light);
    white-space: nowrap;
  }
  .contact__item {
    display: flex;
    align-items: flex-start;
    gap: 8px;
  }
  .contact__icon {
    width: 18px;
    height: 18px;
    margin-top: 3px;
    flex: none;
    fill: var(--ink-light);
  }
</style>
</head>
<body>
<main class="canvas">
  <section class="card card--front" aria-label="Business card front">
    <div class="brand">
      <span class="brand__dot"></span>
      <span class="brand__name">Ferncrest Dental, LLC</span>
    </div>
  </section>

  <section class="card card--back" aria-label="Business card back">
    <div class="back-emblem" role="img" aria-label="Faint brand emblem area"></div>
    <h1 class="holder">Dr. Lorna Pettigrew</h1>
    <ul class="contact">
      <li class="contact__item">
        <svg class="contact__icon" viewBox="0 0 24 24" aria-hidden="true">
          <path d="M12 2a7 7 0 0 0-7 7c0 5 7 13 7 13s7-8 7-13a7 7 0 0 0-7-7zm0 9.5A2.5 2.5 0 1 1 12 6.5a2.5 2.5 0 0 1 0 5z"/>
        </svg>
        <span>2871 Marlowe Street<br>Harrowgate, VT 05999</span>
      </li>
      <li class="contact__item">
        <svg class="contact__icon" viewBox="0 0 24 24" aria-hidden="true">
          <path d="M6.6 10.8a15 15 0 0 0 6.6 6.6l2.2-2.2a1 1 0 0 1 1-.25 11.4 11.4 0 0 0 3.6.57 1 1 0 0 1 1 1V20a1 1 0 0 1-1 1A17 17 0 0 1 3 4a1 1 0 0 1 1-1h3.5a1 1 0 0 1 1 1c0 1.250.2 2.45.57 3.57a1 1 0 0 1-.25 1z"/>
        </svg>
        <span>555-555-0193</span>
      </li>
      <li class="contact__item">
        <svg class="contact__icon" viewBox="0 0 24 24" aria-hidden="true">
          <path d="M3 6h18v12H3z M3 6l9 7 9-7" fill="none" stroke="#ffffff" stroke-width="2" stroke-linejoin="round"/>
        </svg>
        <span>ferncrestdental.office@examplemail.test</span>
      </li>
    </ul>
  </section>
</main>
</body>
</html>
```